Dravel

We are openıng one huntıng showroom in Riyadh? Saudi Arabia. Company name is "DRAVEL".
Our logo designed and we need Business Card Design now.
I attached DRAVEL logo below.
Front side will English and back side will be Arabic

```html
<!DOCTYPE html>
<html lang="en">
<head>
<meta charset="utf-8">
<title>Dravel Business Card</title>
<link href="https://fonts.googleapis.com/css2?family=Montserrat:wght@400;700&family=Noto+Kufi+Arabic:wght@400;600&display=swap" rel="stylesheet">
<style>
  :root {
    --page-bg: #3a3a37;
    --card-bg: #1c1c1c;
    --green: #1f8c47;
    --green-light: #7db544;
    --text-white: #f2f2f2;
    --text-grey: #d6d6d6;
  }
  * { margin: 0; padding: 0; box-sizing: border-box; }
  html, body { width: 1200px; height: 824px; overflow: hidden; }
  body {
    background: var(--page-bg);
    display: flex;
    align-items: center;
    justify-content: center;
    gap: 40px;
    font-family: "Montserrat", sans-serif;
  }
  .card {
    position: relative;
    width: 540px;
    height: 310px;
    background: var(--card-bg);
    color: var(--text-white);
    overflow: hidden;
  }
  .identity {
    position: absolute;
    top: 34px;
    left: 32px;
    padding-left: 12px;
    border-left: 4px solid var(--green);
  }
  .identity .name {
    font-weight: 700;
    font-size: 19px;
    letter-spacing: 0.5px;
    line-height: 1.2;
  }
  .identity .job-title {
    font-size: 12px;
    color: var(--green-light);
    margin-top: 3px;
  }
  .contact-list {
    position: absolute;
    left: 32px;
    top: 138px;
    list-style: none;
    font-size: 12.5px;
    color: var(--text-grey);
  }
  .contact-list li {
    display: flex;
    align-items: center;
    gap: 8px;
    height: 21px;
  }
  .contact-list .icon { width: 12px; height: 12px; flex: none; }
  .contact-list .address { line-height: 1.4; height: auto; margin-top: 4px; display: block; }
  .brand {
    position: absolute;
    right: 30px;
    bottom: 28px;
    display: flex;
    align-items: center;
    gap: 10px;
    direction: ltr;
    font-family: "Montserrat", sans-serif;
    font-weight: 700;
    font-size: 26px;
    line-height: 1;
    color: var(--green);
  }
  .brand-square {
    width: 14px;
    height: 14px;
    background: var(--green);
  }
  .card-back { direction: rtl; font-family: "Noto Kufi Arabic", sans-serif; }
  .card-back .identity .name { font-weight: 600; font-size: 17px; letter-spacing: 0; }
  .card-back .identity .job-title { font-size: 11px; }
  .card-back .contact-list { left: auto; right: 330px; font-size: 12px; }
</style>
</head>
<body>

  <section class="card card-back" lang="ar">
    <div class="identity">
      <p class="name">الاسم الكامل</p>
      <p class="job-title">عنوان وظيفي</p>
    </div>
    <ul class="contact-list">
      <li>
        <svg class="icon" viewBox="0 0 12 12"><path fill="#1f8c47" d="M1 4c0-2 2-3 5-3s5 1 5 3v1H8.5V3.8h-5V5H1zM3 6h6l1.5 5h-9z"/></svg>
        <span>هاتف</span>
      </li>
      <li>
        <svg class="icon" viewBox="0 0 12 12"><rect x="0.5" y="2" width="11" height="8" fill="#1f8c47"/><path d="M0.5 2l5.5 4.5L11.5 2" stroke="#1c1c1c" fill="none"/></svg>
        <span>البريد الإلكتروني</span>
      </li>
      <li>
        <svg class="icon" viewBox="0 0 12 12"><circle cx="6" cy="6" r="5.5" fill="#1f8c47"/></svg>
        <span>موقع إلكتروني</span>
      </li>
      <li class="address">عنوانك<br>الرياض - البريد</li>
    </ul>
    <div class="brand"><span class="brand-square"></span><span class="brand-name">Dravel</span></div>
  </section>

  <section class="card card-front">
    <div class="identity">
      <p class="name">YOUR NAME</p>
      <p class="job-title">Job Title</p>
    </div>
    <ul class="contact-list">
      <li>
        <svg class="icon" viewBox="0 0 12 12"><path fill="#1f8c47" d="M1 4c0-2 2-3 5-3s5 1 5 3v1H8.5V3.8h-5V5H1zM3 6h6l1.5 5h-9z"/></svg>
        <span>000 000 0000</span>
      </li>
      <li>
        <svg class="icon" viewBox="0 0 12 12"><rect x="0.5" y="2" width="11" height="8" fill="#1f8c47"/><path d="M0.5 2l5.5 4.5L11.5 2" stroke="#1c1c1c" fill="none"/></svg>
        <span>youremail@address</span>
      </li>
      <li>
        <svg class="icon" viewBox="0 0 12 12"><circle cx="6" cy="6" r="5.5" fill="#1f8c47"/></svg>
        <span>www.yourwebsite.com</span>
      </li>
      <li class="address">0000, Anywhere, Somewhere<br>Riyadh 0000</li>
    </ul>
    <div class="brand"><span class="brand-square"></span><span class="brand-name">Dravel</span></div>
  </section>

</body>
</html>
```